Business Card Design Project

Hello- I am an interior stylist/product designer whose work is detail driven, very clean and transitional in style and I want my business card to reflect those qualities. I have a logo that I use on my website- my name and a hand drawn chandelier that I want incorporated into the design. However, "Design for the Home" needs to be changed to "Designs". I will be using cream colored stock and am thinking of gray text and logo. I need your help in pulling my card together since it will be the most used element and drive the design of the rest of my stationary suite.
Updates

Please note that I have changed my QR code from my cell # to my website. The new code will be downloaded now.

Reason: I want to thank everyone who has submitted designs- there are truly some very inspiring designs and I am very pleased. I want to make certain that I get this right and have an attractive and highly effective marketing tool when we are finished. With that said, I have run into a technical problem with one aspect of the card- a qr code for my website that was not part of the original brief. I will get that corrected today and post. Once I get that taken care of, I will post comments to all designs received do far. Thanks again for everyone's efforts, Risa

QR Code for the website is now uploaded. Thanks for your patience!

Target Market(s)

Upper middle class- mostly women

Industry/Entity Type

Business

Requirements
Must have
• Marisa Vantry Designs
"...in every small touch."
214-555-0148
marisavantry@plumwick.net
www.marisavantrydesigns-example.com
27083 Birchmont Court
Dallas, TX 75000
Nice to have
• Risa Vantry
Owner

```html
<!DOCTYPE html>
<html lang="en">
<head>
<meta charset="utf-8">
<title>Marisa Vantry Designs — Business Card</title>
<link rel="stylesheet" href="https://fonts.googleapis.com/css2?family=Arimo:ital@0;1&family=Sorts+Mill+Goudy:ital@0;1&display=swap">
<style>
  :root {
    --card-white: #ffffff;
    --paper-tint: #f3f3f2;
    --paper-tint-light: #f8f8f7;
    --slate: #56625f;
    --slate-text: #4d5957;
    --sage-muted: #8d9a98;
  }
  * { margin: 0; padding: 0; box-sizing: border-box; }
  html, body { width: 1200px; height: 750px; overflow: hidden; background: var(--card-white); }
  .card {
    position: relative;
    width: 1200px;
    height: 750px;
    background: var(--card-white);
    font-family: "Arimo", Arial, sans-serif;
    color: var(--slate-text);
  }
  .header { position: absolute; inset: 0 0 auto 0; height: 320px; }
  .brand-name {
    position: absolute; left: 0; width: 1156px; top: 160px;
    text-align: center;
    font-family: "Sorts Mill Goudy", Georgia, serif;
    font-size: 54px; line-height: 1;
    color: var(--slate-text);
  }
  .brand-sub {
    position: absolute; left: 0; width: 1156px; top: 232px;
    text-align: center; font-size: 20px; line-height: 1;
    color: var(--sage-muted);
  }
  .tagline {
    position: absolute; left: 0; width: 1156px; top: 266px;
    text-align: center;
    font-size: 18px; line-height: 1;
    letter-spacing: 0.5px;
    color: var(--slate-text);
  }
  .divider { position: absolute; left: 0; top: 320px; width: 1200px; height: 9px; background: var(--slate); }
  .lower-texture {
    position: absolute; left: 0; top: 329px; width: 1200px; height: 421px;
    background: radial-gradient(ellipse at 50% 40%, var(--paper-tint-light) 0%, var(--paper-tint) 100%);
  }
  .contact {
    position: absolute; left: 0; top: 0; width: 1130px;
    text-align: center;
  }
  .contact p { position: absolute; left: 0; width: 100%; line-height: 1; }
  .person-name { top: 356px; font-size: 38px; }
  .person-role { top: 405px; font-size: 30px; font-style: italic; }
  .phone { top: 470px; font-size: 24px; }
  .address-1 { top: 511px; font-size: 24px; }
  .address-2 { top: 545px; font-size: 24px; }
  .email { top: 592px; font-size: 24px; }
  .website { top: 626px; font-size: 24px; }
</style>
</head>
<body>
  <main class="card">
    <header class="header">
      <div class="brand-name">Marisa Vantry</div>
      <div class="brand-sub">Designs</div>
      <div class="tagline">“…in every small touch.”</div>
    </header>
    <div class="divider"></div>
    <div class="lower-texture" role="img" aria-label="Faint pale grey damask scroll pattern across the lower card area"></div>
    <section class="contact">
      <p class="person-name">Risa Vantry</p>
      <p class="person-role">owner</p>
      <p class="phone">214-555-0148</p>
      <p class="address-1">27083 Birchmont Court</p>
      <p class="address-2">Dallas, TX 75000</p>
      <p class="email">marisavantry@plumwick.net</p>
      <p class="website">www.marisavantrydesigns-example.com</p>
    </section>
  </main>
</body>
</html>
```